This is for a plastic credit card type business card for handing out to clients. It only has the web

I'm looking for a two sided card. This will be printed on a credit card type plastic, ie rounded edges. On the one side is the design. On the other 10 Codes.

The front. A design that is funky but still appropriate for someone in their 30's to 60's The words "Venturers Pledge" "Dorit Velkin" must appear on the front. At the bottom in small writing (Portrait) is www.velkincorp.com

So I'm really looking for the design of the top of the card in making my decision.

On the back of the card in portrait is the following copy.

Heading in Bold is "Venturers Pledge"

I will always remember my WHY
I am an agent for growth and prosperity
I really deserve success in my life
I always stand up again
I will reach out for support on my journey
I will lend fellow entrepreneurs support on their journey
I have the gift of a flexible mind
I see opportunity where others don't
I use my fears to drive me forward
I see success and failure as a learning opportunity

AT THE BOTTOM OF BACK OF THE CARD IS

www.velkincorp.com

```html
<!DOCTYPE html>
<html lang="en">
<head>
<meta charset="utf-8">
<title>Dorit Velkin – Venturers Pledge Card</title>
<link href="https://fonts.googleapis.com/css2?family=Lato:wght@400;700&display=swap" rel="stylesheet">
<style>
  :root {
    --card-blue: #1f74b8;
    --band-blue: #29a8e0;
    --line-blue: #2f9fdc;
    --ink-white: #ffffff;
    --page: #ffffff;
  }
  * { margin: 0; padding: 0; box-sizing: border-box; }
  html, body {
    width: 1200px; height: 640px; overflow: hidden;
    background: var(--page);
    font-family: "Lato", Arial, sans-serif;
  }
  .canvas { position: relative; width: 1200px; height: 640px; }

  .card {
    position: absolute; top: 186px;
    width: 498px; height: 284px;
    border-radius: 20px;
    background: var(--card-blue);
    overflow: hidden;
  }
  .card--front { left: 88px; }
  .card--back { left: 614px; }

  /* Front */
  .front-band {
    position: absolute; left: 0; right: 0; top: 90px; height: 93px;
    background: var(--band-blue);
  }
  .front-rule {
    position: absolute; left: 232px; right: 0; top: 81px; height: 2px;
    background: var(--line-blue);
  }
  .brand-mark {
    position: absolute; left: 60px; top: 118px;
    display: flex; align-items: center; gap: 10px;
    color: var(--card-blue);
    font-weight: 400; font-size: 38px; line-height: 1;
  }
  .brand-mark__square {
    width: 14px; height: 14px; background: var(--card-blue);
  }
  .holder-name {
    position: absolute; left: 258px; top: 118px;
    color: var(--card-blue);
    font-weight: 700; font-size: 35px; line-height: 1; letter-spacing: -0.5px;
  }
  .holder-tagline {
    position: absolute; left: 258px; top: 155px;
    color: var(--card-blue);
    font-size: 15px; line-height: 1;
  }
  .front-url {
    position: absolute; left: 319px; top: 184px;
    color: var(--ink-white);
    font-size: 15px; line-height: 1;
  }

  /* Back */
  .back-band {
    position: absolute; left: 0; right: 0; top: 22px; height: 58px;
    background: var(--band-blue);
  }
  .back-rule {
    position: absolute; left: 0; right: 0; top: 78px; height: 2px;
    background: var(--line-blue);
  }
  .pledge-heading {
    position: absolute; left: 14px; top: 48px;
    color: var(--card-blue);
    font-weight: 700; font-size: 32px; line-height: 1; letter-spacing: -1px;
  }
  .pledge-list {
    position: absolute; left: 0; right: 0; top: 89px;
    list-style: none; text-align: center;
    color: var(--ink-white);
    font-size: 14px; line-height: 15.7px;
  }
  .back-url {
    position: absolute; left: 0; right: 0; top: 253px;
    text-align: center;
    color: var(--ink-white);
    font-size: 15px; line-height: 1;
  }
</style>
</head>
<body>
<main class="canvas">
  <section class="card card--front" aria-label="Card front">
    <div class="front-rule"></div>
    <div class="front-band"></div>
    <div class="brand-mark"><span class="brand-mark__square"></span>Velkin</div>
    <h1 class="holder-name">Dorit Velkin</h1>
    <p class="holder-tagline">_Venturers Pledge</p>
    <p class="front-url">www.velkincorp.com</p>
  </section>

  <section class="card card--back" aria-label="Card back">
    <div class="back-band"></div>
    <div class="back-rule"></div>
    <h2 class="pledge-heading">Venturers Pledge</h2>
    <ul class="pledge-list">
      <li>I will always remember my WHY</li>
      <li>I am an agent for growth and prosperity</li>
      <li>I really deserve success in my life</li>
      <li>I always stand up again</li>
      <li>I will reach out for support on my journey</li>
      <li>I will lend fellow entrepreneurs support on their journey</li>
      <li>I have the gift of a flexible mind</li>
      <li>I see opportunity where others don't</li>
      <li>I use my fears to drive me forward</li>
      <li>I see success and failure as a learning opportunity</li>
    </ul>
    <p class="back-url">www.velkincorp.com</p>
  </section>
</main>
</body>
</html>
```